Design Letterhead, Business Card and ID Card

I need minimalistic design for Letterhead, Business Card and ID Card. Simple and elegant design. Dumny text for address, phone number etc. Logo file attached

```html
<!DOCTYPE html>
<html lang="en">
<head>
<meta charset="utf-8">
<title>Plum Orchard — Business Card</title>
<link href="https://fonts.googleapis.com/css2?family=Open+Sans:wght@400;600&display=swap" rel="stylesheet">
<style>
  :root {
    --backdrop: #ebe4dc;
    --card: #ffffff;
    --ink: #1f1f1f;
    --plum: #8a3a9c;
    --shadow: rgba(90, 70, 50, 0.18);
  }
  * { margin: 0; padding: 0; box-sizing: border-box; }
  html, body {
    width: 1200px; height: 685px; overflow: hidden;
    background: var(--backdrop);
    font-family: "Open Sans", Arial, sans-serif;
    color: var(--ink);
  }
  .stage {
    width: 1200px; height: 685px;
    display: flex; align-items: center; justify-content: center; gap: 60px;
  }
  .card {
    position: relative;
    width: 500px; height: 286px;
    background: var(--card);
    box-shadow: 0 6px 20px var(--shadow);
  }
  .brand {
    display: flex; align-items: center; gap: 10px;
    font-size: 26px; font-weight: 400; color: var(--ink);
    letter-spacing: 0.5px;
  }
  .brand-dot {
    width: 16px; height: 16px; border-radius: 50%;
    background: var(--plum);
  }
  .card--front .brand {
    position: absolute; left: 50%; top: 50%;
    transform: translate(-50%, -50%);
  }
  .card--back .brand {
    position: absolute; right: 36px; top: 44px;
  }
  .contact {
    position: absolute; left: 40px; top: 110px;
    padding-left: 16px;
    border-left: 2px solid var(--plum);
  }
  .person-name {
    font-size: 17px; font-weight: 400; color: var(--plum);
    text-transform: uppercase; letter-spacing: 0.5px;
  }
  .person-role { font-size: 11px; margin-bottom: 8px; }
  .contact-line { font-size: 11px; line-height: 1.55; }
  .address { margin-top: 8px; }
</style>
</head>
<body>
<main class="stage">
  <section class="card card--front">
    <div class="brand"><span class="brand-dot"></span>plum orchard</div>
  </section>

  <section class="card card--back">
    <div class="brand"><span class="brand-dot"></span>plum orchard</div>
    <div class="contact">
      <p class="person-name">Mira Dalton</p>
      <p class="person-role">Project Manager</p>
      <p class="contact-line">(555)014-2286</p>
      <p class="contact-line">hello@plumorchard.com</p>
      <p class="contact-line">www.plumorchard.com</p>
      <div class="address">
        <p class="contact-line">482 Larkin Avenue Oakvale</p>
        <p class="contact-line">FL 30412, US</p>
      </div>
    </div>
  </section>
</main>
</body>
</html>
```